Contemporary new French wine brand needs logo and series of label design

to design a new contemporary logo and series of labels for a new French wine brand. We hope to attract not just current French wine drinkers but new ones who may appreciate a less traditional and more modern style.
Updates

Reason: we are wanting to extend the project for a few days more to receive more submissions since we had fewer designs submitted than we were expecting, maybe because of the holidays.

Target Market(s)

people who follow the arts community (eg. music, theatre, visual/video arts, dance) --- all mature ages.

Industry/Entity Type

French Wine

Requirements
Must have
• a clear, memorable treatment for the name CLAVINE with accompanying logo.
Nice to have
• embossing, matte/gloss refinement, tasteful foil stamping, coated stock for the whites to help the integrity of the paper in and out of ice buckets. A combo of say, three types of fonts; a semi custom font for the brand name Clavine and maybe a script and one other.
Should not have
• not traditional French

```html
<!DOCTYPE html>
<html lang="fr">
<head>
<meta charset="utf-8">
<title>Clavine – Val de Loire label series</title>
<link rel="stylesheet" href="https://fonts.googleapis.com/css2?family=Josefin+Sans:wght@300&family=Great+Vibes&family=Libre+Baskerville&display=swap">
<style>
  :root {
    --backdrop-top: #7a7a7a;
    --backdrop-bottom: #5e5e5e;
    --ink-black: #0f0f0f;
    --band-black-light: #2a2a2a;
    --silver-light: #f2f2f2;
    --silver-mid: #c9c9c9;
    --silver-dark: #a9a9a9;
    --region-red: #c0212f;
    --script-dark: #1a1a1a;
    --script-light: #ffffff;
    --wordmark-light: #e6e6e6;
    --wordmark-dark: #2b2b2b;
    --wave-muscadet: #3f9c7e;
    --wave-cabernet: #b3122a;
    --wave-sauvignon: #3cb8e0;
    --wave-viognier: #5a66c4;
  }
  * { box-sizing: border-box; margin: 0; padding: 0; }
  html, body { width: 1200px; height: 1065px; overflow: hidden; }
  body {
    background: linear-gradient(180deg, var(--backdrop-top), var(--backdrop-bottom));
    display: flex;
    align-items: center;
    justify-content: center;
  }
  .label-series {
    display: grid;
    grid-template-columns: repeat(4, 260px);
    gap: 26px;
  }
  .label {
    width: 260px;
    height: 328px;
    display: flex;
    flex-direction: column;
    box-shadow: 0 6px 18px rgba(0,0,0,0.35);
  }
  .brand-band {
    height: 140px;
    display: flex;
    flex-direction: column;
    align-items: center;
    padding-top: 10px;
    background: linear-gradient(90deg, var(--ink-black), var(--band-black-light) 50%, var(--ink-black));
  }
  .brand-mark {
    width: 44px;
    height: 44px;
    border-radius: 50%;
    border: 2px solid var(--silver-mid);
    background: var(--ink-black);
  }
  .brand-name {
    font-family: "Josefin Sans", sans-serif;
    font-weight: 300;
    font-size: 54px;
    line-height: 1;
    margin-top: 12px;
    letter-spacing: 2px;
    color: var(--wordmark-light);
  }
  .wine-panel {
    flex: 1;
    display: flex;
    flex-direction: column;
    align-items: center;
    padding-top: 14px;
    background: linear-gradient(90deg, var(--silver-dark), var(--silver-light) 45%, var(--silver-mid));
  }
  .region {
    font-family: "Libre Baskerville", serif;
    font-size: 10px;
    letter-spacing: 1.5px;
    color: var(--region-red);
  }
  .varietal {
    font-family: "Great Vibes", cursive;
    font-size: 28px;
    line-height: 1.2;
    margin-top: 12px;
    color: var(--script-dark);
  }
  .wave-band {
    margin-top: auto;
    width: 100%;
    height: 98px;
  }
  .label--muscadet .wave-band { background: linear-gradient(170deg, transparent 10%, var(--wave-muscadet) 60%, transparent 100%); opacity: 0.55; }
  .label--sauvignon .wave-band { background: linear-gradient(170deg, transparent 10%, var(--wave-sauvignon) 60%, transparent 100%); opacity: 0.55; }
  .label--viognier .wave-band { background: linear-gradient(170deg, transparent 10%, var(--wave-viognier) 60%, transparent 100%); opacity: 0.55; }

  /* Red wine: inverted palette */
  .label--cabernet .brand-band {
    background: linear-gradient(90deg, var(--silver-dark), var(--silver-light) 45%, var(--silver-mid));
  }
  .label--cabernet .brand-name { color: var(--wordmark-dark); }
  .label--cabernet .wine-panel {
    background: linear-gradient(90deg, var(--ink-black), var(--band-black-light) 50%, var(--ink-black));
  }
  .label--cabernet .varietal { color: var(--script-light); }
  .label--cabernet .wave-band { background: linear-gradient(170deg, transparent 10%, var(--wave-cabernet) 60%, transparent 100%); opacity: 0.6; }
</style>
</head>
<body>
  <main class="label-series">
    <article class="label label--muscadet">
      <header class="brand-band">
        <span class="brand-mark"></span>
        <h2 class="brand-name">clavine</h2>
      </header>
      <section class="wine-panel">
        <p class="region">Val de Loire</p>
        <h3 class="varietal">Muscadet</h3>
        <div class="wave-band" role="img" aria-label="Flowing green contour-line wave pattern"></div>
      </section>
    </article>

    <article class="label label--cabernet">
      <header class="brand-band">
        <span class="brand-mark"></span>
        <h2 class="brand-name">clavine</h2>
      </header>
      <section class="wine-panel">
        <p class="region">Val de Loire</p>
        <h3 class="varietal">Cabernet Franc</h3>
        <div class="wave-band" role="img" aria-label="Flowing red contour-line wave pattern"></div>
      </section>
    </article>

    <article class="label label--sauvignon">
      <header class="brand-band">
        <span class="brand-mark"></span>
        <h2 class="brand-name">clavine</h2>
      </header>
      <section class="wine-panel">
        <p class="region">Val de Loire</p>
        <h3 class="varietal">Sauvignon Blanc</h3>
        <div class="wave-band" role="img" aria-label="Flowing light blue contour-line wave pattern"></div>
      </section>
    </article>

    <article class="label label--viognier">
      <header class="brand-band">
        <span class="brand-mark"></span>
        <h2 class="brand-name">clavine</h2>
      </header>
      <section class="wine-panel">
        <p class="region">Val de Loire</p>
        <h3 class="varietal">Viognier</h3>
        <div class="wave-band" role="img" aria-label="Flowing violet-blue contour-line wave pattern"></div>
      </section>
    </article>
  </main>
</body>
</html>
```